Harrowgate Supply Group Business Card Design

The Business Card will be one side only with Harrowgate Supplies Group Logo
Card should have:
Name
Title
Office phone Number
Cell Number
email address
Website
Street Address
Our Slogan is Rugged and Reliable
Looking for something that stands out from other business cards

Target Market(s)

Heavy equipment Lease Company

```html
<!DOCTYPE html>
<html lang="en">
<head>
<meta charset="utf-8">
<title>Harrowgate Supplies Group – Business Card</title>
<link href="https://fonts.googleapis.com/css2?family=Montserrat:wght@300;400;700;800&family=Open+Sans:wght@400&display=swap" rel="stylesheet">
<style>
  :root {
    --navy: #2c2e80;
    --red: #d3202f;
    --ink: #555658;
    --paper: #ffffff;
    --backdrop: #e6e6e8;
  }
  * { margin: 0; padding: 0; box-sizing: border-box; }
  html, body { width: 1200px; height: 1176px; overflow: hidden; background: var(--backdrop); }
  .stage { position: relative; width: 1200px; height: 1176px; }
  .card {
    position: absolute; left: 200px; width: 782px; height: 446px;
    border-radius: 28px; overflow: hidden;
    box-shadow: 0 4px 14px rgba(0,0,0,.18);
  }
  .card-front { top: 112px; background: var(--paper); }
  .card-back { top: 597px; background: var(--navy); }

  .person { position: absolute; left: 54px; top: 56px; font-family: "Montserrat", sans-serif; }
  .person-name { font-size: 32px; line-height: 36px; color: var(--navy); font-weight: 300; letter-spacing: .3px; }
  .person-name strong { font-weight: 700; }
  .person-title { margin-top: 6px; font-size: 20px; color: var(--red); font-weight: 400; letter-spacing: 1px; }
  .person-rule { margin-top: 16px; width: 69px; height: 4px; background: var(--red); }

  .brand {
    position: absolute; right: 44px; top: 78px;
    display: flex; align-items: center; gap: 12px;
    font-family: "Montserrat", sans-serif; font-weight: 800; font-size: 19px;
    color: var(--red); letter-spacing: .2px;
  }
  .brand-dot { width: 22px; height: 22px; border-radius: 50%; background: var(--navy); }

  .contacts { position: absolute; left: 56px; top: 224px; list-style: none; font-family: "Open Sans", sans-serif; font-size: 18px; color: var(--ink); }
  .contacts li { display: flex; align-items: center; height: 33.5px; }
  .contacts li.address { margin-top: 17px; }
  .contacts svg { width: 22px; height: 22px; margin-right: 12px; fill: var(--navy); flex: none; }
  .contacts li.address svg { fill: var(--red); }

  .back-content {
    position: absolute; inset: 0; display: flex; flex-direction: column;
    align-items: center; justify-content: center; padding-top: 40px;
    font-family: "Montserrat", sans-serif; color: #fff; text-align: center;
  }
  .back-brand { font-size: 32px; font-weight: 800; letter-spacing: .3px; }
  .back-slogan { margin-top: 44px; font-size: 19px; font-weight: 700; letter-spacing: -.3px; }
</style>
</head>
<body>
<main class="stage">
  <section class="card card-front">
    <div class="person">
      <h1 class="person-name">YOUR <strong>NAME</strong></h1>
      <p class="person-title">JOB TITLE</p>
      <div class="person-rule"></div>
    </div>

    <div class="brand"><span class="brand-dot"></span>HARROWGATE SUPPLIES GROUP</div>

    <ul class="contacts">
      <li><svg viewBox="0 0 24 24"><path d="M2 9c0-3 4-5 10-5s10 2 10 5v2h-5V8.5c-1.5-.6-3-.8-5-.8s-3.5.2-5 .8V11H2z"/><path d="M6 12l2-3h8l2 3v7H6z"/><circle cx="12" cy="15" r="2" fill="#fff"/></svg>000 000 0000</li>
      <li><svg viewBox="0 0 24 24"><path d="M7 2h10a1 1 0 0 1 1 1v18a1 1 0 0 1-1 1H7a1 1 0 0 1-1-1V3a1 1 0 0 1 1-1zm1 3v12h8V5zm4 13.2a1 1 0 1 0 0 2 1 1 0 0 0 0-2z"/></svg>000 000 0000</li>
      <li><svg viewBox="0 0 24 24"><path d="M2 6h20v13H2zm2 2v.3l8 5.5 8-5.5V8l-8 5.2z"/></svg>youremail@xyz.com</li>
      <li><svg viewBox="0 0 24 24" fill="none" style="fill:none;stroke:var(--navy);stroke-width:1.6"><circle cx="12" cy="12" r="9"/><ellipse cx="12" cy="12" rx="4" ry="9"/><path d="M3 12h18M4.5 7.5h15M4.5 16.5h15"/></svg>www.yourwebsite.com</li>
      <li class="address"><svg viewBox="0 0 24 24"><path d="M12 2a7 7 0 0 0-7 7c0 5 7 13 7 13s7-8 7-13a7 7 0 0 0-7-7zm0 9.5a2.5 2.5 0 1 1 0-5 2.5 2.5 0 0 1 0 5z"/></svg>0000, Street Name, City, ST 00000</li>
    </ul>
  </section>

  <section class="card card-back">
    <div class="back-content">
      <p class="back-brand">HARROWGATE SUPPLIES GROUP</p>
      <p class="back-slogan">RUGGED AND RELIABLE</p>
    </div>
  </section>
</main>
</body>
</html>
```